Lionel Arbusto and Dwight Halvorsen Advertisement

We would like an ad that conveys understated elegance. We are a company that purchases estate jewelry watches and diamonds. We care to a wealthy, upscale clientele.

Target Market(s)

Wealthy upscale.

Industry/Entity Type

It Company

Requirements
Must have
• Elegant Design. Crisp Clean. Attached a doc of how the ad should be arranged.

```html
<!DOCTYPE html>
<html lang="en">
<head>
<meta charset="utf-8">
<title>Lionel Arbusto &amp; Dwight Halvorsen – Ready to Sell</title>
<link rel="stylesheet" href="https://fonts.googleapis.com/css2?family=Cinzel:wght@400;500&family=Montserrat:wght@400;500;600&display=swap">
<style>
  :root {
    --ink: #1c1c1c;
    --muted: #4a4a4a;
    --paper: #ffffff;
    --frost-light: #eef0f2;
    --frost: #e1e3e6;
    --frost-deep: #d2d5d9;
    --disc: #c9c9c9;
    --stone-bright: #f4f4f4;
    --stone-mid: #d9d9d9;
    --stone-shade: #9e9e9e;
    --rule: #9a9a9a;
  }
  html, body {
    margin: 0;
    padding: 0;
    width: 1029px;
    height: 1200px;
    overflow: hidden;
    background: var(--paper);
  }
  .ad {
    position: relative;
    width: 1029px;
    height: 1200px;
    overflow: hidden;
    font-family: "Montserrat", sans-serif;
    color: var(--ink);
  }
  .frost-texture {
    position: absolute;
    inset: 0;
    background:
      linear-gradient(to bottom,
        var(--frost) 0%,
        var(--frost-light) 10%,
        var(--paper) 22%,
        var(--paper) 52%,
        var(--frost-light) 62%,
        var(--frost) 80%,
        var(--frost-deep) 100%);
  }
  .headline {
    position: absolute;
    top: 36px;
    left: 0;
    width: 100%;
    margin: 0;
    text-align: center;
    font-family: "Cinzel", serif;
    font-weight: 400;
    font-size: 70px;
    line-height: 86px;
    letter-spacing: 1px;
    color: var(--ink);
  }
  .feature-disc {
    position: absolute;
    top: 132px;
    left: 228px;
    width: 570px;
    height: 570px;
    border-radius: 50%;
    background: var(--disc);
  }
  .feature-stones {
    position: absolute;
    top: 240px;
    left: 236px;
    width: 580px;
    height: 330px;
    border-radius: 60px 60px 30px 30px;
    background: linear-gradient(160deg, var(--stone-bright) 0%, var(--stone-mid) 45%, var(--stone-bright) 70%, var(--stone-shade) 100%);
  }
  .brand {
    position: absolute;
    top: 716px;
    left: 0;
    width: 100%;
    text-align: center;
  }
  .brand-dot {
    display: block;
    width: 60px;
    height: 60px;
    margin: 0 auto 18px;
    border-radius: 50%;
    border: 2px solid var(--ink);
    box-sizing: border-box;
  }
  .brand-name {
    margin: 0;
    font-family: "Cinzel", serif;
    font-weight: 400;
    font-size: 28px;
    line-height: 34px;
    color: var(--muted);
  }
  .brand-tagline {
    display: flex;
    align-items: center;
    justify-content: center;
    gap: 10px;
    margin-top: 2px;
    font-family: "Cinzel", serif;
    font-size: 12px;
    letter-spacing: 1px;
    color: var(--muted);
  }
  .brand-tagline::before,
  .brand-tagline::after {
    content: "";
    width: 130px;
    height: 1px;
    background: var(--rule);
  }
  .promise {
    position: absolute;
    top: 870px;
    left: 0;
    width: 100%;
    margin: 0;
    text-align: center;
    font-weight: 500;
    font-size: 38px;
    line-height: 48px;
    color: var(--ink);
  }
  .contact {
    position: absolute;
    top: 962px;
    left: 95px;
    right: 40px;
    display: flex;
    align-items: center;
  }
  .contact-phone {
    width: 412px;
    font-weight: 600;
    font-size: 50px;
    letter-spacing: 1px;
  }
  .contact-divider {
    width: 2px;
    height: 118px;
    background: var(--rule);
  }
  .contact-address {
    padding-left: 66px;
    font-style: normal;
    font-weight: 500;
    font-size: 23px;
    line-height: 34px;
    color: var(--ink);
  }
</style>
</head>
<body>
  <main class="ad">
    <div class="frost-texture" role="img" aria-label="Soft silver sparkle texture at top and bottom"></div>
    <h1 class="headline">READY TO SELL?</h1>
    <div class="feature-disc"></div>
    <div class="feature-stones" role="img" aria-label="Three emerald-cut diamonds grouped together"></div>
    <div class="brand">
      <span class="brand-dot"></span>
      <p class="brand-name">Lionel Arbusto &amp; Dwight Halvorsen</p>
      <div class="brand-tagline">YOUR BEST OPTION</div>
    </div>
    <p class="promise">Utmost Discretion By Appointment</p>
    <div class="contact">
      <div class="contact-phone">561.555.0148</div>
      <div class="contact-divider"></div>
      <address class="contact-address">
        Via Serena<br>
        118-B Harbor Lane<br>
        Coral Bay, FL 33410<br>
        support@arbustohalvorsen.com
      </address>
    </div>
  </main>
</body>
</html>
```